Fun Movie poster themed flyer/door hanger for pet waste removal company

Im looking for flyer/door hanger design for my spring marketing campaign. I will upload a example of the theme i would like to go with, its an ad from my friends company. Theme being movie poster.

keeping with the movie poster theme. A general idea I had is below.

General image, mom and dad geared up for war, standing side by side. A small active warzone sign in the ground in front of them. With a poop in the middle and skull n bones in the corners.

Dad is geared up with gloves and utility belt with like odor control bottles and hand sanitizers. Hands holding both. Fear in eyes and expression.

Mom geared like wise but holding a shovel and bucket with a look of exhaustion.

General guideline. Please be creative.

Target Market(s)

Pet owners

Font styles to use
Serif

Requirements
Must have
• A fun feel playing on humor.
• A smooth flowing appeal
• Use provided example as template, leaving room for my marketing tech to ad in all the ad info.
• File must be vector.
• Blue is a very evident color in all my branding.

```html
<!DOCTYPE html>
<html lang="en">
<head>
<meta charset="utf-8">
<title>Scoop Squad Door Hanger</title>
<link href="https://fonts.googleapis.com/css2?family=Roboto+Slab:wght@400;700;900&display=swap" rel="stylesheet">
<style>
  :root{
    --bg-light:#d9d9d9;
    --bg-dark:#a9a9a9;
    --blue-deep:#1d3f93;
    --blue-mid:#2857b8;
    --yellow:#f2c21b;
    --white:#ffffff;
    --paper:#eef1f6;
    --ink:#222a3a;
    --photo-a:#ebe9e5;
    --photo-b:#d8d0c4;
    --photo-c:#c6b597;
  }
  *{margin:0;padding:0;box-sizing:border-box}
  html,body{width:1200px;height:886px;overflow:hidden}
  body{
    background:radial-gradient(ellipse at 55% 40%,var(--bg-light),var(--bg-dark));
    font-family:"Roboto Slab",Georgia,serif;
  }
  .hanger{
    position:absolute;left:445px;top:33px;width:310px;height:820px;
    box-shadow:0 14px 30px rgba(0,0,0,.28);
    overflow:hidden;
  }
  .hanger-art{position:absolute;inset:0}
  .family-photo{
    position:absolute;left:0;top:200px;width:310px;height:272px;
    background:linear-gradient(180deg,var(--photo-a) 0%,var(--photo-b) 60%,var(--photo-c) 100%);
    clip-path:polygon(0 0,100% 0,100% 240px,0 270px);
  }
  .hanger-front{position:absolute;inset:0}
  .brand-mark{
    position:absolute;left:0;right:0;top:148px;text-align:center;
    color:var(--yellow);font-weight:900;font-size:27px;letter-spacing:2px;
    text-transform:uppercase;
  }
  .service-copy{
    position:absolute;left:30px;right:30px;top:508px;color:var(--white);
    text-align:center;font-size:12.5px;line-height:1.5;
  }
  .service-copy p+p{margin-top:12px}
  .contact{
    position:absolute;left:18px;right:18px;top:694px;
    display:flex;justify-content:space-between;align-items:center;
    color:var(--ink);font-size:12px;
  }
  .footer-brand{
    position:absolute;left:0;right:0;top:736px;
    display:flex;justify-content:center;align-items:center;gap:7px;
    color:var(--blue-mid);font-weight:700;font-size:15px;text-transform:uppercase;letter-spacing:1px;
  }
  .footer-dot{width:12px;height:12px;border-radius:50%;background:var(--blue-mid)}
</style>
</head>
<body>
  <div class="hanger">
    <svg class="hanger-art" width="310" height="820" viewBox="0 0 310 820" aria-hidden="true">
      <rect width="310" height="820" fill="#eef1f6"/>
    </svg>

    <div class="family-photo" role="img" aria-label="Photo of a family relaxing in a bright living room with their golden retriever on the rug"></div>

    <svg class="hanger-front" width="310" height="820" viewBox="0 0 310 820" aria-hidden="true">
      <defs>
        <radialGradient id="topGlow" cx="50%" cy="30%" r="70%">
          <stop offset="0" stop-color="#3a8fe0"/>
          <stop offset="1" stop-color="#1d3f93"/>
        </radialGradient>
        <radialGradient id="midGlow" cx="55%" cy="55%" r="65%">
          <stop offset="0" stop-color="#2f86d6"/>
          <stop offset="1" stop-color="#1d3f93"/>
        </radialGradient>
      </defs>
      <path d="M0 0H310V185L155 240L0 185Z" fill="url(#topGlow)"/>
      <path d="M0 185L155 240L310 185" fill="none" stroke="#f2c21b" stroke-width="3"/>
      <circle cx="155" cy="70" r="36" fill="#ffffff" stroke="#173477" stroke-width="3"/>
      <path d="M0 470L310 440V640L0 670Z" fill="url(#midGlow)"/>
      <path d="M0 470L310 440" stroke="#f2c21b" stroke-width="3"/>
      <path d="M0 670L310 640" stroke="#f2c21b" stroke-width="2"/>
      <path d="M0 672L310 642V780L0 800Z" fill="#ffffff"/>
      <path d="M0 800L310 780V820H0Z" fill="#f2c21b"/>
      <path d="M0 796L310 776" stroke="#1d3f93" stroke-width="2"/>
    </svg>

    <div class="brand-mark">Scoop Squad</div>

    <div class="service-copy">
      <p>Coming this spring: one family's war on the backyard minefield. Weekly scooping, fresh lawns, zero casualties.</p>
      <p>Rated G for Grass. Now showing in your yard. Call the squad before you step in it.</p>
    </div>

    <div class="contact">
      <span class="phone">CALL: 555-014-2290</span>
      <span class="web">www.scoopsquad.com</span>
    </div>

    <div class="footer-brand"><span class="footer-dot"></span><span>Scoop Squad</span></div>
  </div>
</body>
</html>
```